ZEPRILO.COM is a premium domain sales company. Our competitors are companies like vastplots.example, getparcels.example, peerwords.example. Our current site is at www.zeprilos.example.

We want to have the ability to search for domains, to highlight special offers and have some testimonials on the index page.

The logo for the site is attached.

Please be sure that the order form fits on the screen without scrolling the page. I want the entire form, including the submit button to fit without any page scrolling.

Delivered product - INDEX PAGE, ORDER FORM AND CONTENT PAGE PSDs.

Target Market(s)

Small to Medium business professionals

Industry/Entity Type

It Company

Requirements
Must have
• 1. List of domains for sale
2. Simple search box with button to run the search
3. link for advanced search
4. testimonial area. Note - this can be a small box where a different testimonial is displayed on each page load.
Nice to have
• Would like the site to have some white space. Don't want a heavily packed website. Give it an "airy" feel.

```html
<!DOCTYPE html>
<html lang="en">
<head>
<meta charset="utf-8">
<title>ZEPRILO.COM – Premium Domains</title>
<link rel="stylesheet" href="https://fonts.googleapis.com/css2?family=Source+Sans+3:wght@400;600;700&display=swap">
<style>
  :root {
    --green: #00ac48;
    --green-dark: #0b7a3d;
    --blue: #034d97;
    --link-blue: #1c1cd8;
    --cream: #f3e3a8;
    --ink: #111111;
    --white: #ffffff;
    --chip: #dedede;
  }
  * { box-sizing: border-box; margin: 0; padding: 0; }
  html, body { width: 1200px; height: 1000px; overflow: hidden; background: var(--white); }
  body { font-family: "Source Sans 3", "Myriad Pro", sans-serif; color: var(--ink); position: relative; }
  .abs { position: absolute; }

  .brand { left: 375px; top: 52px; font-size: 30px; font-weight: 700; color: var(--green-dark); letter-spacing: -0.5px; line-height: 1; }

  .main-nav { left: 355px; top: 95px; width: 478px; height: 26px; background: var(--green); display: flex; align-items: center; justify-content: space-around; }
  .main-nav a { color: var(--white); text-decoration: none; font-size: 14px; }

  .hero { left: 355px; top: 122px; width: 478px; height: 251px; background: var(--blue); }
  .hero-visual { position: absolute; left: 11px; top: 15px; width: 202px; height: 221px; background: linear-gradient(180deg, #1a66b8 0%, #0e4d8f 55%, #062b55 100%); }
  .hero-copy { position: absolute; left: 225px; top: 0; width: 240px; color: var(--white); font-size: 13px; text-align: center; }
  .hero-copy p { position: absolute; left: 0; width: 240px; }

  .search-label { left: 372px; top: 411px; font-size: 13px; }
  .search-box { left: 355px; top: 435px; width: 263px; height: 68px; background: var(--blue); border-radius: 8px; }
  .search-input { position: absolute; left: 11px; top: 13px; width: 186px; height: 18px; color: var(--white); font-size: 13px; padding-left: 25px; border-bottom: 2px solid var(--cream); }
  .advanced-search { left: 355px; top: 480px; width: 131px; height: 43px; background: var(--green); border-radius: 4px; color: var(--white); font-size: 13px; padding: 13px 0 0 17px; }

  .domain-table { left: 365px; top: 538px; width: 255px; }
  .table-head { position: absolute; top: 0; color: var(--link-blue); font-size: 15px; }
  .table-rule { position: absolute; left: 10px; top: 21px; width: 233px; height: 2px; background: var(--blue); }
  .row { position: absolute; left: 0; width: 255px; height: 20px; }
  .row .name { position: absolute; left: 0; font-size: 10px; }
  .row .price { position: absolute; left: 124px; font-size: 10px; }
  .row .price.big { font-size: 13px; }
  .row .buy { position: absolute; left: 203px; font-size: 13px; }

  .testimonial-tab { left: 643px; top: 436px; width: 34px; height: 124px; background: var(--green-dark); border-radius: 3px; color: var(--white); font-size: 8px; font-weight: 600; text-align: center; line-height: 9.6px; padding-top: 5px; }
  .testimonial { left: 671px; width: 161px; height: 88px; background: var(--green); border-radius: 4px; font-size: 7.5px; }
  .testimonial p { position: absolute; left: 14px; width: 140px; line-height: 15px; }
  .testimonial.dark-text p { color: var(--ink); top: 6px; }
  .testimonial.light-text p { color: var(--white); top: 9px; left: 0; width: 161px; text-align: center; font-weight: 600; }
  .author { position: absolute; right: 3px; bottom: 4px; background: var(--chip); border-radius: 3px; padding: 3px 9px; font-size: 8px; color: var(--ink); }
  .author.lg { font-size: 9.5px; padding: 3px 5px; }

  .happy-customer { left: 650px; top: 690px; width: 183px; height: 213px; background: radial-gradient(ellipse at 50% 55%, #e03a3a 0%, #f2b9a0 45%, #ffffff 75%); }

  .site-footer { left: 355px; top: 904px; width: 478px; height: 57px; background: var(--blue); }
  .social { position: absolute; top: 16px; width: 28px; height: 27px; background: var(--chip); border-radius: 5px; }
  .copyright { position: absolute; left: 395px; top: 22px; color: var(--white); font-size: 9px; }
</style>
</head>
<body>
  <div class="abs brand">ZEPRILO</div>

  <nav class="abs main-nav">
    <a href="#">Home</a><a href="#">Contact Us</a><a href="#">Domains Sale</a><a href="#">Testimonials</a><a href="#">Cart</a>
  </nav>

  <section class="abs hero">
    <div class="hero-visual" role="img" aria-label="Photo of business people at a meeting table beneath a glowing world map"></div>
    <div class="hero-copy">
      <p style="top:31px">Let’ s your Door is wide open to the world</p>
      <p style="top:76px">by Buying this PREMIUM DOMAIN !</p>
      <p style="top:130px">Impression of Your business could be</p>
      <p style="top:186px">started from Name of the Domain its self.</p>
    </div>
  </section>

  <div class="abs search-label">Search for a Domain</div>
  <div class="abs search-box"><div class="search-input">Enter name of Domain</div></div>
  <div class="abs advanced-search">Advance search</div>

  <div class="abs domain-table">
    <span class="table-head" style="left:11px">DOMAIN</span>
    <span class="table-head" style="left:124px">PRIZE</span>
    <span class="table-head" style="left:213px">BUY</span>
    <div class="table-rule"></div>
    <div class="row" style="top:48px"><span class="name">DomainName1.com</span><span class="price big">$1,005</span><span class="buy">Buy now</span></div>
    <div class="row" style="top:102px"><span class="name">DomainName2.com</span><span class="price big">$2,015</span><span class="buy">Buy now</span></div>
    <div class="row" style="top:156px"><span class="name">DomainName3.com</span><span class="price">$3,025</span><span class="buy">Buy now</span></div>
    <div class="row" style="top:208px"><span class="name">DomainName4.com</span><span class="price">$4,035</span><span class="buy">Buy now</span></div>
    <div class="row" style="top:257px"><span class="name">DomainName5.com</span><span class="price">$5,045</span><span class="buy">Buy now</span></div>
  </div>

  <div class="abs testimonial-tab">T<br>E<br>S<br>T<br>I<br>M<br>O<br>N<br>I<br>A<br>L<br>S</div>
  <div class="abs testimonial dark-text" style="top:412px">
    <p>We would like to thank to ZEPRILO.COM<br>for a georgeous name Domain that<br>We were looking for.</p>
    <span class="author">Mr Tal Renn</span>
  </div>
  <div class="abs testimonial light-text" style="top:504px">
    <p>Thank to ZEPRILO.COM ,<br>We are satisfy&nbsp; with the Domain name<br>we bought from you.</p>
    <span class="author lg">Vantor Corp</span>
  </div>

  <div class="abs happy-customer" role="img" aria-label="Photo of a cheering woman in a red top with raised fists"></div>

  <footer class="abs site-footer">
    <span class="social" style="left:25px" role="img" aria-label="Social network link"></span>
    <span class="social" style="left:65px" role="img" aria-label="Social network link"></span>
    <span class="copyright">Copyrights 2013</span>
  </footer>
</body>
</html>
```